Business card - Kestrel Bay Framing

Design a business card utilizing the given logo.
colors we like: Black, greys, Teal, blues.
Tri color card, horizontal orientation likely
Logo and name likely best on top.
Info on card:

Dennis Harcourt
#5 - 1845 Larchmont Way
Surrey, B.C. V7T 3K2

604.555.0193
dennisharcourt@telvane.ca

Slogan: "Building Dreams"

We are a construction company that specializes in new home construction on the West coast of BC Canada. Bay Framing designs of high end homes.

```html
<!DOCTYPE html>
<html lang="en">
<head>
<meta charset="utf-8">
<title>Kestrel Bay Framing – Business Card</title>
<link rel="stylesheet" href="https://fonts.googleapis.com/css2?family=Michroma&family=Roboto:wght@400&display=swap">
<style>
  :root {
    --backdrop: #6b6b6b;
    --card-white: #ffffff;
    --teal: #05b0a0;
    --ink: #111111;
    --on-teal: #ffffff;
  }
  html, body {
    margin: 0;
    width: 1200px;
    height: 1000px;
    overflow: hidden;
    background: var(--backdrop);
  }
  .business-card {
    position: absolute;
    left: 150px;
    top: 222px;
    width: 900px;
    height: 555px;
    background: var(--teal);
    box-shadow: 0 4px 14px rgba(0,0,0,0.35);
    overflow: hidden;
  }
  .brand-band {
    position: absolute;
    left: 0; top: 0;
    width: 100%;
    height: 202px;
    background: var(--card-white);
    display: flex;
    align-items: center;
    justify-content: center;
    gap: 26px;
  }
  .brand-dot {
    width: 104px;
    height: 104px;
    border-radius: 50%;
    background: var(--ink);
  }
  .brand-name {
    font-family: "Michroma", sans-serif;
    font-size: 40px;
    color: var(--ink);
    letter-spacing: 1px;
    text-transform: uppercase;
    line-height: 1;
  }
  .holder {
    position: absolute;
    left: 480px;
    top: 240px;
    color: var(--on-teal);
  }
  .holder-name {
    font-family: "Michroma", sans-serif;
    font-size: 34px;
    margin: 0;
    letter-spacing: 1px;
    line-height: 1.1;
  }
  .holder-title {
    font-family: "Roboto", sans-serif;
    font-size: 21px;
    margin: 6px 0 0;
  }
  .contact-list {
    position: absolute;
    left: 78px;
    top: 410px;
    margin: 0;
    padding: 0;
    list-style: none;
    font-family: "Roboto", sans-serif;
    font-size: 22px;
    color: var(--on-teal);
  }
  .contact-list li {
    display: flex;
    align-items: center;
    gap: 12px;
    height: 33px;
  }
  .contact-icon {
    width: 21px;
    height: 21px;
    flex: none;
  }
</style>
</head>
<body>
  <div class="business-card">
    <header class="brand-band">
      <span class="brand-dot"></span>
      <span class="brand-name">Kestrel Bay Framing</span>
    </header>

    <div class="holder">
      <p class="holder-name">Dennis Harcourt</p>
      <p class="holder-title">Managing Director</p>
    </div>

    <ul class="contact-list">
      <li>
        <svg class="contact-icon" viewBox="0 0 20 20" aria-hidden="true">
          <rect width="20" height="20" rx="3" fill="#fff"/>
          <path d="M6 4h3l1 4-2 1.5a8 8 0 0 0 3 3L12.5 11l4 1v3a2 2 0 0 1-2 2A11 11 0 0 1 4 6a2 2 0 0 1 2-2z" fill="var(--teal)"/>
        </svg>
        <span>604.555.0193</span>
      </li>
      <li>
        <svg class="contact-icon" viewBox="0 0 20 20" aria-hidden="true">
          <rect width="20" height="20" rx="3" fill="#fff"/>
          <rect x="4" y="6" width="12" height="8" rx="1" fill="var(--teal)"/>
        </svg>
        <span>dennisharcourt@telvane.ca</span>
      </li>
      <li>
        <svg class="contact-icon" viewBox="0 0 20 20" aria-hidden="true">
          <rect width="20" height="20" rx="3" fill="#fff"/>
          <path d="M10 3a5 5 0 0 1 5 5c0 4-5 9-5 9s-5-5-5-9a5 5 0 0 1 5-5z" fill="var(--teal)"/>
          <circle cx="10" cy="8" r="2" fill="#fff"/>
        </svg>
        <span>#5 - 1845 Larchmont Way Surrey, B.C. V7T 3K2</span>
      </li>
    </ul>
  </div>
</body>
</html>
```